The Timber Loft

We need a business card design for our wardrobe company.
Please visit our website www.zorvelcabinets.com to get an idea of who we are.

```html
<!DOCTYPE html>
<html lang="en">
<head>
<meta charset="utf-8">
<title>The Timber Loft – Business Card</title>
<link href="https://fonts.googleapis.com/css2?family=Poppins:wght@400;500;600&display=swap" rel="stylesheet">
<style>
  :root {
    --backdrop: #e9e6e2;
    --card-white: #ffffff;
    --card-black: #000000;
    --ink: #111111;
    --text-light: #ffffff;
  }
  html, body {
    margin: 0;
    padding: 0;
    width: 1200px;
    height: 989px;
    overflow: hidden;
    background: var(--backdrop);
    font-family: "Poppins", sans-serif;
  }
  .card {
    position: absolute;
    left: 50px;
    top: 178px;
    width: 1100px;
    height: 632px;
    background: var(--card-white);
    box-shadow: 0 6px 18px rgba(0,0,0,0.18);
    overflow: hidden;
  }
  .card-shape {
    position: absolute;
    inset: 0;
    width: 100%;
    height: 100%;
  }
  .brand-mark {
    position: absolute;
    left: 340px;
    top: 134px;
    width: 96px;
    height: 96px;
    border: 5px solid var(--ink);
    box-sizing: border-box;
  }
  .brand-text {
    position: absolute;
    left: 466px;
    top: 136px;
    width: 390px;
    color: var(--ink);
    text-align: center;
  }
  .brand-name {
    font-size: 30px;
    font-weight: 500;
    line-height: 44px;
    letter-spacing: 0.3px;
  }
  .brand-tagline {
    font-size: 25px;
    font-weight: 600;
    line-height: 40px;
    margin-top: 5px;
  }
  .contact {
    position: absolute;
    left: 0;
    right: 0;
    top: 426px;
    color: var(--text-light);
    text-align: center;
  }
  .contact-person {
    margin: 0;
    line-height: 52px;
  }
  .person-name {
    font-size: 40px;
    font-weight: 500;
    letter-spacing: 0.5px;
  }
  .person-role {
    font-size: 28px;
    font-weight: 500;
  }
  .contact-line {
    margin: 0;
    font-size: 26px;
    font-weight: 400;
    line-height: 36px;
  }
  .contact-address { margin-top: 8px; }
  .contact-phone { margin-top: 7px; }
  .contact-web { margin-top: -2px; }
</style>
</head>
<body>
  <div class="card">
    <svg class="card-shape" viewBox="0 0 1100 632" preserveAspectRatio="none" aria-hidden="true">
      <path d="M0,240 Q550,520 1100,240 L1100,632 L0,632 Z" fill="var(--card-black)"/>
      <path d="M4,250 Q550,530 1096,250" fill="none" stroke="var(--card-white)" stroke-width="2"/>
    </svg>

    <div class="brand-mark"></div>
    <div class="brand-text">
      <div class="brand-name">THE TIMBER LOFT</div>
      <div class="brand-tagline">Crafted to Fit Your Home</div>
    </div>

    <div class="contact">
      <p class="contact-person"><span class="person-name">Daniel Hartley</span> <span class="person-role">– President</span></p>
      <p class="contact-line contact-address">Orrin Court, 42 Marlow Street, London N4 7QT</p>
      <p class="contact-line contact-phone">P. 020 8146 3075 E. info@zorvelcabinets.com</p>
      <p class="contact-line contact-web">www.zorvelcabinets.com</p>
    </div>
  </div>
</body>
</html>
```